Website for small historic hotel called the Corbett Crown

We are looking to design a website for a small Inn/Hotel.
Site would need to be able to take reservations and flow through to booking via Tallypay with orchard pay, quorra pay and zunmi pay (Chinese verson )
We would have links from Velora, Vorbo.com, roam critic etc to our website for booking purposes
Here are some examples of small inn/hotels doing the same sort of thing in our area. Provided purely for reference, not to be plagiarized!
https://innbrackwell.example/tollivers/
https://www.dunmorecourt.example/hotel
https://www.falconinnbrackwell.example/hotel
https://www.thewendover.example/
We will also provide you some photos, once the site has been done, to utilize instead of random shots taken from the internet as placeholders
I have also provided a link to some hotels in Perthshire Scotland which may also provide you with some ideas Again please do not plagiarise
https://glenvarrowlodge.example/
https://www.theinnatcraigbrannoch.example/
https://www.fennickheadhotel.example/
http://www.northern-hostelries.example/HighlandsandBorders.htm
Our inn is in 12 Harrow Lane, Mitchell Falls NOT Scotland but the original owner was a Corbett from Perthshire Scotland and is responsible for the county being named Perth
We would need a landing page plus the following
page for rooms
Page for booking
Contact page
About US Page
Total site is landing page plus 4 or 5 sub pages
The general outline is provided. Please contact me with specific questions
Just as an update the folllowing are the placeholder names for the pages. They will be tabs at the top right and fllow through to sub pages off the main landing page
MAIN LANDING PAGE links at top to
1 _ history - the story of the building and Corbett
2_ Contact
3_ Rooms and Suites - will have each room and suite and link to sub-page for each
4 _ Perth County
5 - to be determined
The following would be sub pages
3 will display links to the suites: with a sub-page for each suite
Garden Suite - includes a 500 square foot patio and garden
Reception Suite - under renovation
Parlour Suite - Old parlor - Under renovation
GRAYMOORHAVEN Suite - Under renovation
1854 Suite 0- Under renovation
Updates
Just some additional information
The Inn/Hotel this website is for is named after a native of Perthshire Scotland who is also responsible for the area being names Perth County
The building is constructed in the 1850's and the decor and design are those of small-town inns you can find in the British Isles - England, Scotonal, Ireland and Wales
Some examples from Perthshire in Scotland - for inspiration, not plagiarisation!
https://glenvarrowlodge.example/
Please note the inn does not have a restaurant at present and only offers rooms
Feel free to submitt any questions for clarification
I have also provided a link to some hotels in Perthshire Scotland with similar designs and crests as well as to give you some background as to Perth. Again please do not plagiarise
https://glenvarrowlodge.example/
This is provided as an outline and we can answer specific questions
Few if any designs of any quality were received. Really nowhere near what was promised and certainly not the quality or quantity I would expect KT, whom I worked with before and I invited, submitted the bulk of the entries
Industry/Entity Type
boutique hotel - 19th century traditional British Isles
Number of Pages Required
5+ page
Look and feel
Each slider illustrates characteristics of the customer's brand and the style your logo design should communicate.

```html
<!DOCTYPE html>
<html lang="en">
<head>
<meta charset="utf-8">
<title>Corbett Crown Hotel, Perth</title>
<link href="https://fonts.googleapis.com/css2?family=Cormorant+Garamond:wght@400;500&family=Libre+Baskerville&display=swap" rel="stylesheet">
<style>
:root{
  --green:#6c8a4f;
  --ink:#2b2b2b;
  --text:#444;
  --muted:#9a9a9a;
  --soft:#f3f3ee;
  --footer:#333333;
  --white:#ffffff;
}
*{box-sizing:border-box;margin:0;padding:0}
html,body{width:1200px;height:5034px;overflow:hidden}
body{position:relative;background:var(--white);font-family:"Libre Baskerville",Georgia,serif;color:var(--text)}
.abs{position:absolute}
.serif{font-family:"Cormorant Garamond",Georgia,serif}
.photo{position:absolute}
.btn{position:absolute;background:var(--green);color:var(--white);font-size:12px;letter-spacing:.5px;display:flex;align-items:center;justify-content:center;text-transform:uppercase}
.h2{position:absolute;left:0;width:1200px;text-align:center;font-family:"Cormorant Garamond",Georgia,serif;font-size:44px;color:var(--ink);font-weight:500}
.sub{position:absolute;left:0;width:1200px;text-align:center;font-family:"Cormorant Garamond",Georgia,serif;font-size:28px;color:#555}
.para{position:absolute;font-size:13.2px;line-height:22px;color:var(--text)}
.hero{left:0;top:0;width:1200px;height:641px;background:linear-gradient(160deg,#3a3430 0%,#5b5450 35%,#8e8a86 55%,#4a3e34 80%,#2e2620 100%)}
.logo{left:127px;top:44px;color:var(--white);font-family:"Cormorant Garamond",Georgia,serif;font-size:36px;letter-spacing:1px}
.nav a{position:absolute;top:56px;color:var(--white);font-size:13px;text-decoration:none;letter-spacing:.5px}
.hero-title{left:0;width:1200px;top:226px;text-align:center;color:var(--white);font-family:"Cormorant Garamond",Georgia,serif;font-size:58px}
.arrow{position:absolute}
.booking{left:0;top:580px;width:1051px;height:141px;background:var(--white);box-shadow:0 4px 10px rgba(0,0,0,.06)}
.booking label{position:absolute;top:35px;font-size:15px;color:#555}
.field{position:absolute;top:65px;height:39px;border:1px solid #ccc;font-size:10px;color:#777;padding:12px 10px}
.check{left:873px;top:0;width:178px;height:141px;background:var(--green);color:var(--white);font-size:17px;text-align:center;display:flex;align-items:center;justify-content:center;line-height:22px}
.partner{position:absolute;top:795px;font-family:"Cormorant Garamond",Georgia,serif;font-size:48px;color:#b5b5b5;display:flex;align-items:center;gap:10px}
.dot{width:30px;height:30px;border-radius:50%;background:#c4c4c4}
.rooms-bg{left:0;top:1555px;width:1200px;height:764px;background:var(--soft)}
.card-name{position:absolute;top:2060px;width:280px;text-align:center;font-family:"Cormorant Garamond",Georgia,serif;font-size:26px;color:var(--ink)}
.card-text{position:absolute;top:2100px;width:280px;text-align:center;font-size:12.5px;line-height:19px;color:var(--text)}
.county{left:0;top:2319px;width:1200px;height:487px;background:linear-gradient(180deg,#8ea2b8 0%,#b7c4cf 28%,#6e7f72 45%,#9a8a3c 60%,#6f6a2a 78%,#7b7f84 100%)}
.about-side{left:0;top:2806px;width:395px;height:633px;background:var(--soft)}
.contact{left:0;top:3439px;width:1200px;height:475px;background:var(--green)}
.input{position:absolute;border:1px solid rgba(255,255,255,.7);color:var(--white);font-size:12px;padding:12px 10px}
.footer{left:0;top:4684px;width:1200px;height:350px;background:var(--footer);color:var(--white)}
.footer .fnav{position:absolute;top:50px;font-size:14px;transform:translateX(-50%);letter-spacing:.5px}
.finfo{position:absolute;top:134px;font-size:13px;display:flex;align-items:center;gap:8px;white-space:nowrap}
.social{position:absolute;top:281px;width:22px;height:22px;border-radius:50%;border:2px solid var(--white)}
</style>
</head>
<body>

<div class="abs hero" role="img" aria-label="Dimly lit hotel bedroom with a made bed, lamps and dark wood floor"></div>
<div class="abs logo">CORBETT CROWN</div>
<nav class="nav">
  <a style="left:520px">HOME</a>
  <a style="left:619px">ROOMS</a>
  <a style="left:729px">BOOKING</a>
  <a style="left:856px">CONTACT</a>
  <a style="left:993px">ABOUT US</a>
</nav>
<h1 class="abs hero-title" style="font-weight:400">Corbett Crown Hotel, Perth</h1>
<div class="btn" style="left:539px;top:336px;width:121px;height:43px;font-size:13px">Book now</div>
<svg class="arrow" style="left:56px;top:314px" width="24" height="34" viewBox="0 0 24 34"><path d="M18 3 5 17l13 14" fill="none" stroke="#fff" stroke-width="4"/></svg>
<svg class="arrow" style="left:1134px;top:314px" width="24" height="34" viewBox="0 0 24 34"><path d="M6 3l13 14L6 31" fill="none" stroke="#fff" stroke-width="4"/></svg>

<section class="abs booking">
  <label style="left:92px">Arrive:</label>
  <label style="left:305px">Arrive:</label>
  <label style="left:516px">Rooms</label>
  <label style="left:619px">Adults</label>
  <label style="left:719px">Children</label>
  <div class="field" style="left:92px;width:195px">dd-mm-yyyy</div>
  <div class="field" style="left:305px;width:195px">dd-mm-yyyy</div>
  <div class="field" style="left:516px;width:88px">1</div>
  <div class="field" style="left:619px;width:88px">1</div>
  <div class="field" style="left:719px;width:88px">1</div>
  <svg class="abs" style="left:262px;top:79px" width="12" height="12" viewBox="0 0 12 12"><rect x="1" y="2" width="10" height="9" fill="none" stroke="#888"/><line x1="1" y1="5" x2="11" y2="5" stroke="#888"/></svg>
  <svg class="abs" style="left:475px;top:79px" width="12" height="12" viewBox="0 0 12 12"><rect x="1" y="2" width="10" height="9" fill="none" stroke="#888"/><line x1="1" y1="5" x2="11" y2="5" stroke="#888"/></svg>
  <svg class="abs" style="left:584px;top:81px" width="10" height="8"><path d="M1 2l4 4 4-4" fill="none" stroke="#888"/></svg>
  <svg class="abs" style="left:687px;top:81px" width="10" height="8"><path d="M1 2l4 4 4-4" fill="none" stroke="#888"/></svg>
  <svg class="abs" style="left:787px;top:81px" width="10" height="8"><path d="M1 2l4 4 4-4" fill="none" stroke="#888"/></svg>
  <div class="abs check">CHECK<br>AVAILABILITY</div>
</section>

<div class="partner" style="left:238px"><span class="dot"></span>roam critic</div>
<div class="partner" style="left:570px">Velora</div>
<div class="partner" style="left:766px">Vorbo.com</div>

<h2 class="h2" style="top:928px">Welcome to Corbett Crown Hotel, Perth</h2>
<p class="sub" style="top:986px">Lorem ipsum dolor sit amet, consectetur</p>
<div class="photo" style="left:150px;top:1073px;width:432px;height:349px;background:linear-gradient(180deg,#4b4a3a 0%,#8a7a55 45%,#3f8f9e 70%,#6fc6d4 100%)" role="img" aria-label="Hotel courtyard with palm trees and a lit swimming pool at dusk"></div>
<h3 class="abs serif" style="left:637px;top:1092px;font-size:36px;font-weight:500;color:var(--ink)">History</h3>
<p class="para" style="left:637px;top:1150px;width:420px">Lorem ipsum dolor sit amet, consectetur adipiscing elit, sedo eiusmod tempor incididunt ut labore et dolore magna aliqua. Quis ipsum suspendisse ultrices gravida. Risus commodo vive rra maecenas accumsan lacus vel facilisis. Lorem ipsum door sit amet, consectetur adipiscing elit, sed do eiusmod tempor incididunt ut labore et dolore magna aliquauis ipsumlorems suspendisse ultrices gravidaisus commodo vive loremispdm rra maecenas accumsan lacus vel facilisis.</p>
<div class="btn" style="left:639px;top:1342px;width:121px;height:43px">Read more</div>

<section class="abs rooms-bg"></section>
<h2 class="h2" style="top:1632px">Rooms and Suites</h2>
<p class="sub" style="top:1684px">Lorem ipsum dolor sit amet, consectetur</p>
<svg class="arrow" style="left:90px;top:1893px" width="20" height="32"><path d="M16 2 4 16l12 14" fill="none" stroke="#777" stroke-width="3"/></svg>
<svg class="arrow" style="left:1082px;top:1893px" width="20" height="32"><path d="M4 2l12 14L4 30" fill="none" stroke="#777" stroke-width="3"/></svg>

<div class="photo" style="left:150px;top:1759px;width:280px;height:283px;background:linear-gradient(180deg,#3d5a2a 0%,#55693c 45%,#5e564c 70%,#3b2e22 100%)" role="img" aria-label="Lounge with a living green wall, sofa and coffee table"></div>
<div class="photo" style="left:459px;top:1759px;width:280px;height:283px;background:linear-gradient(180deg,#e9e6e0 0%,#9c8466 45%,#4a4540 75%,#2f2c29 100%)" role="img" aria-label="Reception desk with wood panelling and ring pendant lights"></div>
<div class="photo" style="left:768px;top:1759px;width:281px;height:283px;background:linear-gradient(180deg,#e5e6e4 0%,#c9c4bb 45%,#a37a55 75%,#6f6f6f 100%)" role="img" aria-label="Bright parlour with a leather sofa and large windows"></div>

<div class="card-name" style="left:150px">Garden Suite</div>
<div class="card-name" style="left:459px">Reception Suite</div>
<div class="card-name" style="left:768px">Parlour Suite</div>
<p class="card-text" style="left:150px">Lorem ipsum dolor sit amet, cons ctur adipiscing elit, sed do eiusmod por incididunt ut laboredo</p>
<p class="card-text" style="left:459px">Lorem ipsum dolor sit amet, cons ctur adipiscing elit, sed do eiusmod por incididunt ut laboredo</p>
<p class="card-text" style="left:768px">Lorem ipsum dolor sit amet, cons ctur adipiscing elit, sed do eiusmod por incididunt ut laboredo</p>
<div class="btn" style="left:229px;top:2179px;width:123px;height:43px">Read more</div>
<div class="btn" style="left:538px;top:2179px;width:123px;height:43px">Read more</div>
<div class="btn" style="left:847px;top:2179px;width:123px;height:43px">Read more</div>

<section class="abs county" role="img" aria-label="Autumn forest hills above a lake and winding road"></section>
<h2 class="abs serif" style="left:623px;top:2470px;font-size:44px;font-weight:400;color:var(--white)">Perth County</h2>
<p class="abs" style="left:623px;top:2544px;width:490px;font-size:19.5px;line-height:30px;color:var(--white)">Lorem ipsum dolor sit amet, consectetur adipisc ing elit, sed do eiusmod tempor incididunt ut labore et dolore magna aliqua.</p>

<section class="abs about-side"></section>
<svg class="abs" style="left:229px;top:2900px" width="310" height="432" viewBox="0 0 310 432" role="img" aria-label="Portrait of the hotel owner">
  <defs><linearGradient id="portrait" x1="0" y1="0" x2="0" y2="1"><stop offset="0" stop-color="#c9a27a"/><stop offset=".5" stop-color="#e2c3a5"/><stop offset="1" stop-color="#f2f0ec"/></linearGradient></defs>
  <path d="M0 432V155A155 155 0 0 1 310 155V432Z" fill="#6c8a4f"/>
  <path d="M12 432V160A143 143 0 0 1 298 160V432Z" fill="url(#portrait)"/>
</svg>
<h2 class="abs serif" style="left:636px;top:2958px;font-size:44px;font-weight:400;color:var(--ink)">About Corbett</h2>
<p class="para" style="left:637px;top:3023px;width:420px">Lorem ipsum dolor sit amet, consectetur adipiscing elit, sedo eiusmod tempor incididunt ut labore et dolore magna aliqua. Quis ipsum suspendisse ultrices gravida. Risus commodo vive rra maecenas accumsan lacus vel facilisis. Lorem ipsum door sit amet, consectetur adipiscing elit, sed do eiusmod tempor incididunt ut labore et dolore magna aliquauis ipsumlorems suspendisse ultrices gravidaisus commodo vive loremispdm rra maecenas accumsan lacus vel facilisis.</p>
<div class="btn" style="left:639px;top:3216px;width:121px;height:43px">Read more</div>

<section class="abs contact"></section>
<h2 class="abs serif" style="left:150px;top:3584px;font-size:44px;font-weight:400;color:var(--white)">Contact Us</h2>
<p class="abs" style="left:150px;top:3660px;width:340px;font-size:13.2px;line-height:21px;color:var(--white)">Lorem ipsum dolor sit amet, consectetur adipiscing elit, sedo eiusmod tempor incididunt ut labore et dolore magna aliqua.</p>
<div class="input" style="left:612px;top:3562px;width:195px;height:43px">Name</div>
<div class="input" style="left:818px;top:3562px;width:194px;height:43px">Phone</div>
<div class="input" style="left:612px;top:3613px;width:195px;height:43px">Email</div>
<div class="input" style="left:818px;top:3613px;width:194px;height:43px">Subject</div>
<div class="input" style="left:612px;top:3664px;width:400px;height:99px">Message</div>
<div class="abs" style="left:897px;top:3740px;width:103px;height:41px;background:var(--white);color:var(--green);font-size:12px;display:flex;align-items:center;justify-content:center">SUBMIT</div>

<svg class="abs" style="left:0;top:3914px" width="1200" height="770"><polygon points="0,770 0,730 1200,40 1200,770" fill="#f2f2ec"/></svg>
<h2 class="h2" style="top:4004px;font-weight:400">to be Determined</h2>
<p class="abs" style="left:280px;top:4076px;width:640px;text-align:center;font-size:13.2px;line-height:22px;color:var(--text)">Lorem ipsum dolor sit amet, consectetur adipiscing elit, sedo eiusmod tempor incididunt ut labore et dolore magna aliqua. Quis ipsum suspendisse ultrices gravida.</p>
<div class="photo" style="left:148px;top:4168px;width:272px;height:307px;background:linear-gradient(180deg,#6a5440 0%,#b79a78 45%,#efe9e0 70%,#8a6a4a 100%)" role="img" aria-label="Hotel room with a bed and warm lighting"></div>
<div class="photo" style="left:463px;top:4168px;width:274px;height:307px;background:linear-gradient(180deg,#2f4a78 0%,#6d86b0 40%,#2fb3c9 70%,#d08a4a 100%)" role="img" aria-label="Outdoor pool lit at twilight"></div>
<div class="photo" style="left:778px;top:4168px;width:273px;height:307px;background:linear-gradient(180deg,#a9a096 0%,#d6cfc4 45%,#3a3532 75%,#6a5644 100%)" role="img" aria-label="Modern bedroom with upholstered headboard and bedside lamps"></div>
<p class="abs" style="left:148px;top:4500px;width:272px;text-align:center;font-size:15px;line-height:22px;color:var(--text)">Lorem ipsum dolor sit amet, consectetur adipiscing</p>
<p class="abs" style="left:463px;top:4500px;width:274px;text-align:center;font-size:15px;line-height:22px;color:var(--text)">Lorem ipsum dolor sit amet, consectetur adipiscing</p>
<p class="abs" style="left:778px;top:4500px;width:273px;text-align:center;font-size:15px;line-height:22px;color:var(--text)">Lorem ipsum dolor sit amet, consectetur adipiscing</p>

<footer class="abs footer">
  <span class="fnav" style="left:309px">HOME</span>
  <span class="fnav" style="left:434px">ROOMS</span>
  <span class="fnav" style="left:571px">BOOKING</span>
  <span class="fnav" style="left:721px">CONTACT</span>
  <span class="fnav" style="left:873px">ABOUT US</span>
  <div class="finfo" style="left:200px"><svg width="14" height="14" viewBox="0 0 24 24"><path d="M6.6 10.8a15 15 0 0 0 6.6 6.6l2.2-2.2a1 1 0 0 1 1-.25 11 11 0 0 0 3.6.6 1 1 0 0 1 1 1V20a1 1 0 0 1-1 1A17 17 0 0 1 3 4a1 1 0 0 1 1-1h3.5a1 1 0 0 1 1 1 11 11 0 0 0 .6 3.6 1 1 0 0 1-.25 1z" fill="#fff"/></svg>Phone: 555 010 0188</div>
  <div class="finfo" style="left:430px"><svg width="14" height="12" viewBox="0 0 14 12"><rect width="14" height="12" fill="#fff"/><path d="M0 0l7 6 7-6" fill="none" stroke="#333" stroke-width="1.5"/></svg>Email:info@corbettcrown.example</div>
  <div class="finfo" style="left:735px"><svg width="12" height="16" viewBox="0 0 12 16"><path d="M6 0a6 6 0 0 1 6 6c0 4-6 10-6 10S0 10 0 6a6 6 0 0 1 6-6z" fill="#fff"/><circle cx="6" cy="6" r="2.2" fill="#333"/></svg>12 Harrow Lane, Mitchell Falls</div>
  <p class="abs" style="left:0;top:222px;width:1200px;text-align:center;font-size:13.5px">Copyright © 2022 Corbett Crown Hotel | &nbsp;Privacy Policy | Terms and Conditions</p>
  <span class="social" style="left:499px"></span>
  <span class="social" style="left:558px"></span>
  <span class="social" style="left:616px"></span>
  <span class="social" style="left:675px"></span>
</footer>

</body>
</html>
```